Velmin & Co Powerpoint Template

A simple powerpoint template for my business which provides management consulting services for Business Owners.

It should reflect the colours within the logo design and should work as the master template for all standard powerpoint slide layouts.

```html
<!DOCTYPE html>
<html lang="en">
<head>
<meta charset="utf-8">
<title>Velmin &amp; Co — Presentation Template</title>
<link rel="stylesheet" href="https://fonts.googleapis.com/css2?family=Montserrat:wght@300;400;500;600&family=Open+Sans:wght@400;600;700&display=swap">
<style>
:root{
  --orange:#e4602f;
  --black:#000;
  --white:#fff;
  --page:#f2f2f2;
  --ink:#3c3c3c;
  --panel:#dcdcdc;
  --c-blue:#5b9bd5;
  --c-orange:#ed7d31;
  --c-grey:#a5a5a5;
  --c-gold:#ffc000;
}
*{box-sizing:border-box;margin:0;padding:0}
html,body{width:913px;height:1200px;overflow:hidden;background:var(--page)}
.canvas{position:relative;width:913px;height:1200px;background:var(--page);font-family:"Open Sans",Arial,sans-serif;color:var(--ink)}
.slide{position:absolute;width:368.5px;height:207.6px;overflow:hidden;background:var(--white);box-shadow:0 1px 3px rgba(0,0,0,.12)}
.col-l{left:68.5px}.col-r{left:476.6px}
.row1{top:46px}.row2{top:269px}.row3{top:501px}.row4{top:723px}.row5{top:956px}
.slide--dark{background:var(--black)}
.slide--orange{background:var(--orange)}
.abs{position:absolute}

.headline-bar{position:absolute;left:0;top:17px;width:24.5px;height:5.5px;background:var(--orange)}
.headline{position:absolute;left:30.5px;top:12px;font:400 9px/1 "Montserrat",Arial,sans-serif;color:var(--orange);letter-spacing:.1px}
.slide--orange .headline-bar,.on-orange .headline-bar{background:var(--white)}
.slide--orange .headline,.on-orange .headline{color:var(--white)}

.page-no{position:absolute;right:0;top:182px;width:23.5px;height:18px;background:var(--orange);color:var(--white);font:600 4.5px/18px "Open Sans",Arial,sans-serif;text-align:center}
.slide--orange .page-no{background:var(--white);color:var(--orange)}

.leaves-faint{position:absolute;border-radius:50%;background:radial-gradient(ellipse at center,rgba(228,96,47,.09),rgba(228,96,47,0) 70%)}
.leaves-dark{position:absolute;border-radius:50%;background:radial-gradient(ellipse at center,rgba(70,70,70,.55),rgba(40,40,40,0) 70%)}

/* brand name block */
.brand{position:absolute;display:flex;align-items:center;justify-content:center;background:#0d0d0d}
.brand-square{background:var(--orange);flex:none}
.brand-name{font-family:"Montserrat",Arial,sans-serif;font-weight:300;color:var(--white);white-space:nowrap;line-height:1}

/* cover */
.cover-rule{left:24.5px;top:113px;width:40px;height:2px;background:var(--orange)}
.cover-title{left:24.5px;top:119px;font:400 14.2px/1.3 "Montserrat",Arial,sans-serif;color:var(--white)}
.cover-sub{left:24.5px;top:159px;font:400 6.4px/1.65 "Montserrat",Arial,sans-serif;color:var(--orange)}

/* contents */
.toc-title{position:absolute;left:32px;top:15px;font:400 8.8px/1 "Montserrat",Arial,sans-serif;color:var(--orange)}
.toc-item{position:absolute;display:flex;align-items:flex-start}
.toc-num{width:14px;height:14px;border-radius:50%;background:var(--orange);border:1.5px solid #f7c9b6;color:var(--white);font:600 4px/11px "Open Sans",Arial,sans-serif;text-align:center;margin-top:1px}
.toc-text{margin-left:5px;padding-left:2px;border-left:.5px solid #ccc}
.toc-text b{display:block;font:400 7.4px/1.1 "Montserrat",Arial,sans-serif;color:#555}
.toc-text span{display:block;font:400 3.7px/1.35 "Open Sans",Arial,sans-serif;color:#999;width:62px}

/* services */
.service{position:absolute;top:44px;width:76px;text-align:center}
.service-icon{width:46px;height:46px;margin:0 auto;border-radius:50%;background:#4a4a4a;border:2px solid #f3f3f3;display:flex;align-items:center;justify-content:center}
.service-text{margin-top:13px;font:700 4.5px/1.66 "Open Sans",Arial,sans-serif;color:var(--white)}

/* text + photo */
.kicker{left:15px;top:35px;font:400 4.4px/1 "Montserrat",Arial,sans-serif;color:#777}
.small-copy{font:400 3.05px/1.6 "Open Sans",Arial,sans-serif;color:#333}
.small-copy p+p{margin-top:2px}
.photo{position:absolute}
.photo--cloud{background:linear-gradient(135deg,#3c4c66 0%,#7d8ea6 45%,#c9d2dd 60%,#2b3447 100%)}
.photo--office{background:linear-gradient(135deg,#cfd6de 0%,#6f7d8d 50%,#2f3a48 100%)}
.photo--desk{background:linear-gradient(135deg,#e4e8ec 0%,#9aa6b2 55%,#ffffff 100%)}

/* team */
.member-photo{position:absolute;top:37px;width:44px;height:44px;border-radius:50%;border:1px solid #6a9a5a;background:radial-gradient(circle at 50% 40%,#f1f1f1,#9ea4aa)}
.member-card{position:absolute;top:84px;width:92px;height:89px;background:var(--panel);padding:2px 4px;overflow:hidden}
.member-card h3{font:400 4px/1.25 "Open Sans",Arial,sans-serif;color:var(--orange);border-bottom:.4px solid #eee;padding-bottom:2px;margin-bottom:2px}
.member-card p{font:400 3.3px/1.68 "Open Sans",Arial,sans-serif;color:#333}
.col-rule{position:absolute;top:38px;width:.6px;height:135px;background:#f0b8a2}

/* chart */
.chart-title{left:20px;top:35px;width:156px;text-align:center;font:400 7.4px/1.15 "Montserrat",Arial,sans-serif;color:#222}
.legend{left:60px;top:56px;display:flex;gap:4px;font:400 3.6px/1 "Open Sans",Arial,sans-serif;color:#555}
.legend i{display:inline-block;width:2.5px;height:2.5px;margin-right:1px}
.body-just{font:400 5.25px/1.38 "Open Sans",Arial,sans-serif;color:#333;text-align:justify}
.body-just p+p{margin-top:5px}

/* half orange */
.half-orange{position:absolute;left:0;top:0;width:179px;height:207.6px;background:var(--orange)}
.half-lead{left:29px;top:31px;width:146px;font:400 6px/1.15 "Montserrat",Arial,sans-serif;color:var(--white)}
.half-copy{left:29px;top:53px;width:143px;height:148px;overflow:hidden;font:400 3.3px/1.68 "Open Sans",Arial,sans-serif;color:var(--white)}
.half-copy p+p{margin-top:3px}

/* feature list */
.feature-icon{position:absolute;left:153px;width:12px;height:12px;border-radius:50%;border:1px solid var(--orange);background:#f4f4f4;display:flex;align-items:center;justify-content:center}
.feature{position:absolute;left:172px;width:180px}
.feature h4{font:600 5px/1.2 "Open Sans",Arial,sans-serif;color:#666;margin-bottom:3px}
.feature p{font:400 3.3px/1.65 "Open Sans",Arial,sans-serif;color:#333}

/* back cover contact */
.contact{left:86px;top:168px;font:400 3.1px/1.6 "Open Sans",Arial,sans-serif;color:var(--white)}
.contact p+p{margin-top:2px}
</style>
</head>
<body>
<main class="canvas">

  <!-- Cover -->
  <section class="slide slide--dark col-l row1" aria-label="Cover slide">
    <div class="leaves-dark" role="img" aria-label="Faint leaf pattern" style="left:190px;top:100px;width:200px;height:130px"></div>
    <div class="brand" style="left:248px;top:6.5px;width:109px;height:72px">
      <div class="brand-square" style="width:10px;height:10px;margin-right:6px"></div>
      <div class="brand-name" style="font-size:12px">Velmin &amp; Co</div>
    </div>
    <div class="abs cover-rule"></div>
    <h1 class="abs cover-title">Lorem ipsum dolor sit<br>amet, consectetuer</h1>
    <p class="abs cover-sub">Lorem ipsum dolor sit amet, consectetuer<br>adipiscing elit, sed diam nonummy</p>
  </section>

  <!-- Contents -->
  <section class="slide col-r row1" aria-label="Table of contents">
    <div class="leaves-faint" role="img" aria-label="Faint leaf pattern" style="left:0;top:140px;width:130px;height:90px"></div>
    <div class="headline-bar"></div>
    <h2 class="toc-title">TABLE OF CONTENTS</h2>
    <div class="toc-item" style="left:17.5px;top:40px"><div class="toc-num">1</div><div class="toc-text"><b>About Us</b><span>Lorem Ipsum is simply dummy text of the printing and type-</span></div></div>
    <div class="toc-item" style="left:148px;top:40px"><div class="toc-num">2</div><div class="toc-text"><b>Who We Are</b><span>Lorem Ipsum is simply dummy text of the printing and type-</span></div></div>
    <div class="toc-item" style="left:269.5px;top:40px"><div class="toc-num">3</div><div class="toc-text"><b>What We Do</b><span>Lorem Ipsum is simply dummy text of the printing and type-</span></div></div>
    <div class="toc-item" style="left:17.5px;top:74px"><div class="toc-num">4</div><div class="toc-text"><b>About Us</b><span>Lorem Ipsum is simply dummy text of the printing and type-</span></div></div>
    <div class="toc-item" style="left:148px;top:74px"><div class="toc-num">5</div><div class="toc-text"><b>About Us</b><span>Lorem Ipsum is simply dummy text of the printing and type-</span></div></div>
    <div class="toc-item" style="left:269.5px;top:74px"><div class="toc-num">6</div><div class="toc-text"><b>About Us</b><span>Lorem Ipsum is simply dummy text of the printing and type-</span></div></div>
    <div class="toc-item" style="left:17.5px;top:109.5px"><div class="toc-num">7</div><div class="toc-text"><b>About Us</b><span>Lorem Ipsum is simply dummy text of the printing and type-</span></div></div>
    <div class="toc-item" style="left:148px;top:109.5px"><div class="toc-num">8</div><div class="toc-text"><b>About Us</b><span>Lorem Ipsum is simply dummy text of the printing and type-</span></div></div>
    <div class="toc-item" style="left:269.5px;top:109.5px"><div class="toc-num">9</div><div class="toc-text"><b>About Us</b><span>Lorem Ipsum is simply dummy text of the printing and type-</span></div></div>
    <div class="toc-item" style="left:17.5px;top:143px"><div class="toc-num">7</div><div class="toc-text"><b>About Us</b><span>Lorem Ipsum is simply dummy text of the printing and type-</span></div></div>
    <div class="toc-item" style="left:148px;top:143px"><div class="toc-num">8</div><div class="toc-text"><b>About Us</b><span>Lorem Ipsum is simply dummy text of the printing and type-</span></div></div>
    <div class="toc-item" style="left:269.5px;top:143px"><div class="toc-num">9</div><div class="toc-text"><b>About Us</b><span>Lorem Ipsum is simply dummy text of the printing and type-</span></div></div>
    <div class="page-no">1</div>
  </section>

  <!-- Services -->
  <section class="slide slide--orange col-l row2" aria-label="Services slide">
    <div class="leaves-faint" role="img" aria-label="Faint leaf pattern" style="left:0;top:150px;width:130px;height:70px;background:radial-gradient(ellipse at center,rgba(255,255,255,.18),rgba(255,255,255,0) 70%)"></div>
    <div class="headline-bar"></div>
    <h2 class="headline">PLACE HEADLINE HERE</h2>
    <div class="service" style="left:12.5px">
      <div class="service-icon" role="img" aria-label="Handshake icon"></div>
      <p class="service-text">Lorem Ipsum is simply dummy text of the printing and typesetting industry. Lorem Ipsum has been Lorem Ipsum is simply dummy text of the printing and typesetting industry. Lorem Ipsum has been</p>
    </div>
    <div class="service" style="left:98.5px">
      <div class="service-icon" role="img" aria-label="Support agent icon"></div>
      <p class="service-text">Lorem Ipsum is simply dummy text of the printing and typesetting industry. Lorem Ipsum has been Lorem Ipsum is simply dummy text of the printing and typesetting industry. Lorem Ipsum has been</p>
    </div>
    <div class="service" style="left:185px">
      <div class="service-icon">
        <svg width="24" height="24" viewBox="0 0 24 24" aria-hidden="true"><rect x="5" y="2" width="14" height="20" rx="1.5" fill="none" stroke="#fff" stroke-width="1.8"/><path d="M8 7h8M8 10.5h8M8 14h5M8 17.5l2 2 4-4" fill="none" stroke="#fff" stroke-width="1.5"/></svg>
      </div>
      <p class="service-text">Lorem Ipsum is simply dummy text of the printing and typesetting industry. Lorem Ipsum has been Lorem Ipsum is simply dummy text of the printing and typesetting industry. Lorem Ipsum has been</p>
    </div>
    <div class="service" style="left:276px">
      <div class="service-icon">
        <svg width="26" height="24" viewBox="0 0 26 24" aria-hidden="true"><rect x="3" y="14" width="4" height="8" fill="#fff"/><rect x="9" y="11" width="4" height="11" fill="#fff"/><rect x="15" y="8" width="4" height="14" fill="#fff"/><path d="M3 11 L11 6 L15 8 L22 3" fill="none" stroke="#fff" stroke-width="1.6"/><path d="M19 2.5h3.5v3.5" fill="none" stroke="#fff" stroke-width="1.6"/></svg>
      </div>
      <p class="service-text">Lorem Ipsum is simply dummy text of the printing and typesetting industry. Lorem Ipsum has been Lorem Ipsum is simply dummy text of the printing and typesetting industry. Lorem Ipsum has been</p>
    </div>
    <div class="page-no">3</div>
  </section>

  <!-- Text and photo -->
  <section class="slide col-r row2" aria-label="Text and image slide">
    <div class="leaves-faint" role="img" aria-label="Faint leaf pattern" style="left:0;top:160px;width:120px;height:60px"></div>
    <div class="headline-bar"></div>
    <h2 class="headline">PLACE HEADLINE HERE</h2>
    <p class="abs kicker">PLACE HEADLINE HERE</p>
    <div class="abs small-copy" style="left:15px;top:42px;width:153px;height:130px;overflow:hidden">
      <p>Lorem ipsum dolor sit amet, consectetuer adipiscing elit, sed diam nonummy nibh euismod tincidunt ut laoreet dolore magna aliquam erat volutpat. Ut wisi enim ad minim veniam, quis nostrud exerci tation ullamcorper suscipit lobortis nisl ut aliquip ex ea commodo consequat. Duis autem vel eum iriure dolor in hendrerit in vulputate velit esse molestie consequat.</p>
      <p>Lorem ipsum dolor sit amet, consectetuer adipiscing elit, sed diam nonummy nibh euismod tincidunt ut laoreet dolore magna aliquam erat volutpat. Ut wisi enim ad minim veniam, quis nostrud exerci tation ullamcorper suscipit lobortis nisl ut aliquip ex ea commodo consequat. Duis autem vel eum iriure dolor in hendrerit in vulputate velit esse molestie consequat.</p>
      <p>Lorem ipsum dolor sit amet, consectetuer adipiscing elit, sed diam nonummy nibh euismod tincidunt ut laoreet dolore magna aliquam erat volutpat. Ut wisi enim ad minim veniam, quis nostrud exerci tation ullamcorper suscipit lobortis nisl ut aliquip ex ea commodo consequat. Duis autem vel eum iriure dolor in hendrerit in vulputate velit esse molestie consequat.</p>
    </div>
    <div class="photo photo--cloud" role="img" aria-label="Photo of a businessman sketching cloud computing connections" style="left:181px;top:36px;width:172px;height:136px"></div>
    <div class="page-no">2</div>
  </section>

  <!-- Team -->
  <section class="slide col-l row3" aria-label="Team slide">
    <div class="leaves-faint" role="img" aria-label="Faint leaf pattern" style="left:0;top:150px;width:130px;height:70px"></div>
    <div class="headline-bar"></div>
    <h2 class="headline">PLACE HEADLINE HERE</h2>
    <div class="member-photo" role="img" aria-label="Sample photo of a relaxed businessman" style="left:30px"></div>
    <div class="member-photo" role="img" aria-label="Sample photo of a businesswoman at a desk" style="left:158px"></div>
    <div class="member-photo" role="img" aria-label="Sample photo of a stack of papers" style="left:296px"></div>
    <div class="col-rule" style="left:123px"></div>
    <div class="col-rule" style="left:245px"></div>
    <div class="member-card" style="left:15.8px">
      <h3>Lorem ipsum dolor sit amet, consecte-tur adipisicing elit, sed do eiusmod</h3>
      <p>Lorem Ipsum is simply dummy text of the printing and typesetting industry. Lorem Ipsum has been the industry's standard dummy text ever since the 1500s, when an unknown printer took a galley of type and scrambled it to make a type specimen book. It has survived not only five centuries, but also the leap into electronic typesetting, remaining essentially unchanged.</p>
    </div>
    <div class="member-card" style="left:137.5px">
      <h3>Lorem ipsum dolor sit amet, consectetur adipisicing elit, sed</h3>
      <p>Lorem Ipsum is simply dummy text of the printing and typesetting industry. Lorem Ipsum has been the industry's standard dummy text ever since the 1500s, when an unknown printer took a galley of type and scrambled it to make a type specimen book. It has survived not only five centuries.</p>
    </div>
    <div class="member-card" style="left:258px">
      <h3>Lorem ipsum dolor sit amet, consecte-tur adipisicing elit, sed do eiusmod</h3>
      <p>Lorem Ipsum is simply dummy text of the printing and typesetting industry. Lorem Ipsum has been the industry's standard dummy text ever since the 1500s, when an unknown printer took a galley of type and scrambled it to make a type specimen book. It has survived not only five centuries, but also the leap into electronic typesetting.</p>
    </div>
    <div class="page-no">5</div>
  </section>

  <!-- Chart -->
  <section class="slide col-r row3" aria-label="Chart slide">
    <div class="leaves-faint" role="img" aria-label="Faint leaf pattern" style="left:0;top:150px;width:130px;height:70px"></div>
    <div class="headline-bar"></div>
    <h2 class="headline">PLACE HEADLINE HERE</h2>
    <p class="abs chart-title">USE OF FOUNDER SEED CAPITAL<br>$1.12M SINCE JAN 2014</p>
    <div class="abs legend">
      <span><i style="background:var(--c-blue)"></i>marketing</span>
      <span><i style="background:var(--c-orange)"></i>sg&amp;a</span>
      <span><i style="background:var(--c-grey)"></i>r&amp;d</span>
      <span><i style="background:var(--c-gold)"></i>1x legal</span>
    </div>
    <svg class="abs" style="left:48px;top:74px" width="100" height="100" viewBox="0 0 100 100" role="img" aria-label="Donut chart: r&amp;d 60%, sg&amp;a 21%, marketing 12%, legal 7%">
      <g transform="rotate(-90 50 50)" fill="none" stroke-width="24">
        <circle cx="50" cy="50" r="37" pathLength="100" stroke="#5b9bd5" stroke-dasharray="12 88" stroke-dashoffset="0"/>
        <circle cx="50" cy="50" r="37" pathLength="100" stroke="#ed7d31" stroke-dasharray="21 79" stroke-dashoffset="-12"/>
        <circle cx="50" cy="50" r="37" pathLength="100" stroke="#a5a5a5" stroke-dasharray="60 40" stroke-dashoffset="-33"/>
        <circle cx="50" cy="50" r="37" pathLength="100" stroke="#ffc000" stroke-dasharray="7 93" stroke-dashoffset="-93"/>
      </g>
      <g font-family="Open Sans, Arial, sans-serif" font-size="5" fill="#fff" text-anchor="middle">
        <text x="66" y="14">marketing</text><text x="66" y="20">12%</text>
        <text x="84" y="48">sg&amp;a</text><text x="84" y="54">21%</text>
        <text x="21" y="69">r&amp;d</text><text x="21" y="75">60%</text>
        <text x="42" y="10">legal</text><text x="42" y="16">7%</text>
      </g>
    </svg>
    <div class="abs body-just" style="left:184.5px;top:34px;width:171px;height:140px;overflow:hidden">
      <p>Lorem Ipsum is simply dummy text of the printing and typesetting industry. Lorem Ipsum has been the industry's standard dummy text ever since the 1500s, when an unknown printer took a galley of type and scrambled it to make a type specimen book. It has survived not only five centuries, but also the leap into electronic typesetting, remaining essentially unchanged. It was popularised in the 1960s with the release of sheets containing Lorem Ipsum passages, and more recently with desktop publishing software including many versions of Lorem Ipsum.</p>
      <p>It is a long established fact that a reader will be distracted by the readable content of a page when looking at its layout. The point of using Lorem Ipsum is that it has a more-or-less normal distribution of letters, as opposed to using 'Content here, content here', making it look like readable English. Many desktop publishing packages and web page editors now use Lorem Ipsum as their default model text. Contrary to popular belief, Lorem Ipsum is not simply random text.</p>
    </div>
    <div class="page-no">4</div>
  </section>

  <!-- Half orange with photo -->
  <section class="slide col-l row4 on-orange" aria-label="Split slide with photo">
    <div class="half-orange"></div>
    <div class="photo photo--cloud" role="img" aria-label="Close-up photo of a businessman drawing a cloud diagram" style="left:179px;top:0;width:189.5px;height:207.6px"></div>
    <div class="headline-bar"></div>
    <h2 class="headline">PLACE HEADLINE HERE</h2>
    <p class="abs half-lead">Lorem ipsum dolor sit amet, consectetur adipisic-ing elit, sed do eiusmod tempor incididunt ut</p>
    <div class="abs half-copy">
      <p>Lorem Ipsum is simply dummy text of the printing and typesetting industry. Lorem Ipsum has been the industry's standard dummy text ever since the 1500s, when an unknown printer took a galley of type and scrambled it to make a type specimen book. It has survived not only five centuries, but also the leap into electronic typesetting, remaining essentially unchanged.</p>
      <p>It is a long established fact that a reader will be distracted by the readable content of a page when looking at its layout. The point of using Lorem Ipsum is that it has a more-or-less normal distribution of letters, as opposed to using 'Content here, content here', making it look like readable English. Many desktop publishing packages and web page editors now use Lorem Ipsum as their default model text.</p>
      <p>Contrary to popular belief, Lorem Ipsum is not simply random text. It has roots in a piece of classical Latin literature, making it over 2000 years old. Its passages have been used for centuries in printing, and the words are scrambled so that the reader is not drawn into the meaning of the text.</p>
      <p>The standard chunk of Lorem Ipsum used since the 1500s is reproduced below for those interested, together with a short translation.</p>
    </div>
  </section>

  <!-- Features with photos -->
  <section class="slide col-r row4" aria-label="Feature slide with photos">
    <div class="leaves-faint" role="img" aria-label="Faint leaf pattern" style="left:0;top:160px;width:130px;height:60px"></div>
    <div class="headline-bar"></div>
    <h2 class="headline">PLACE HEADLINE HERE</h2>
    <div class="photo photo--cloud" role="img" aria-label="Photo of a businessman with a cloud sketch" style="left:15.5px;top:33.5px;width:128px;height:76px"></div>
    <div class="photo photo--office" role="img" aria-label="Photo of a businessman relaxing at his desk" style="left:15.5px;top:112px;width:64px;height:57.5px"></div>
    <div class="photo photo--desk" role="img" aria-label="Photo of a man at a computer workstation" style="left:82px;top:112px;width:61.5px;height:57.5px"></div>
    <div class="feature-icon" style="top:33px"><svg width="7" height="7" viewBox="0 0 10 10" aria-hidden="true"><circle cx="5" cy="5" r="3.5" fill="none" stroke="#666" stroke-width="1.2"/></svg></div>
    <div class="feature" style="top:34px">
      <h4>Lorem ipsum dolor sit amet, consectetur adipisicing elit, sed do ei-</h4>
      <p>Lorem Ipsum is simply dummy text of the printing and typesetting industry. Lorem Ipsum has been the industry's standard dummy text ever since the 1500s, when an unknown printer took a galley of type and scrambled it to make a type specimen book. It has survived not only five centuries, but also the leap into electronic typesetting, remaining essentially unchanged. It was popularised in the 1960s with the release of L. It is a long established fact that a reader will be distracted by the readable content of a page when looking at its layout. The point of using Lorem Ipsum is that it has a more-or-less normal distribution of letters, making it look like readable English.</p>
    </div>
    <div class="feature-icon" style="top:110px"><svg width="7" height="7" viewBox="0 0 10 10" aria-hidden="true"><rect x="2" y="5" width="1.6" height="3" fill="#666"/><rect x="4.2" y="3.5" width="1.6" height="4.5" fill="#666"/><rect x="6.4" y="2" width="1.6" height="6" fill="#666"/></svg></div>
    <div class="feature" style="top:111px">
      <h4>Lorem ipsum dolor sit amet, consectetur adipisicing elit, sed do</h4>
      <p>Lorem Ipsum is simply dummy text of the printing and typesetting industry. Lorem Ipsum has been the industry's standard dummy text ever since the 1500s, when an unknown printer took a galley of type and scrambled it to make a type specimen book. It has survived not only five centuries, but also the leap into electronic typesetting, remaining essentially unchanged. It was popularised in the 1960s with the release of L<br>It is a long established fact that a reader will be distracted by the readable content of a page when looking at its layout. The point of using Lorem Ipsum is that it has a more-or-less normal distribution of letters.</p>
    </div>
    <div class="page-no">5</div>
  </section>

  <!-- Back cover -->
  <section class="slide slide--dark col-l row5" aria-label="Back cover">
    <div class="leaves-dark" role="img" aria-label="Faint leaf pattern" style="left:190px;top:100px;width:200px;height:130px"></div>
    <div class="brand" style="left:18.5px;top:168px;width:60px;height:22px;justify-content:flex-start;background:transparent">
      <div class="brand-square" style="width:5px;height:5px;margin-right:3px"></div>
      <div class="brand-name" style="font-size:6.5px">Velmin &amp; Co</div>
    </div>
    <div class="abs contact">
      <p>P: 000-555-0142 Ext 101<br>E: hello@velminco.com<br>W: www.velminco.com</p>
      <p>210, 48 Harbour Lane<br>Northfield ON A1B 2C3</p>
    </div>
  </section>

</main>
</body>
</html>
```